Physical Literacy company needs a web page designed...

We are a new company who provide physical education training to schools and deliver interventions to improve health and wellbeing, academic achievement through physical activity.

We need the website to have the following specification:
Creative design and production for 8 x page website for Movendra. Imagery and text as supplied by client. Fully responsive website design for multiple devices.
– 8 Main pages to website as per attached site plan – Twitter feed on home page
– Social Links - link to blog page
– Content management system for 2 pages
– Site Testing and Implementation
– Cookies policy and legal document templates if necessary

I am attaching a business plan PPT to give you a better idea of business. This should enable you to lift a lot of the content from the PPT also.

Target Market(s)

Physical Education - Schools
Families who wish to be more physically active

Industry/Entity Type

Education

Number of Pages Required

5+ page

Font styles to use
Sans Serif
Other font styles liked:
• Chalkboard

Colors
fbee3e
33a6d7
ec1f27
9bcb3c

Requirements
Must have
• *Home page
• *biog of company and four co-founders - who are well? What do we do? How do we do it? Contact details
• *Content management for two pages - blog page and case studies
• *Live twitter feed
• *links to youtube videos

```html
<!DOCTYPE html>
<html lang="en">
<head>
<meta charset="utf-8">
<title>Movendra – Physical Education Training</title>
<link href="https://fonts.googleapis.com/css2?family=Open+Sans:wght@400;600;700&family=Raleway:wght@600;700;800&display=swap" rel="stylesheet">
<style>
:root{
  --orange:#f0a030;
  --blue:#33a6d7;
  --mustard:#c8c21b;
  --red:#ec1f27;
  --green:#9bcb3c;
  --ink:#222222;
  --body:#555555;
  --muted:#8a8a8a;
  --light:#f4f4f4;
  --grey:#ededed;
  --footer:#252525;
  --footer-deep:#1d1d1d;
  --line:#3a3a3a;
  --brown:#7a4a1c;
}
*{margin:0;padding:0;box-sizing:border-box}
html,body{width:1200px;height:2612px;overflow:hidden}
body{position:relative;font-family:'Open Sans',Arial,sans-serif;color:var(--ink);background:#fff}
.abs{position:absolute}

/* header */
.site-header{left:0;top:0;width:1200px;height:96px;background:#fff}
.brand{left:96px;top:26px;font-weight:700;font-size:32px;letter-spacing:1px;color:var(--orange)}
.main-nav a{position:absolute;top:38px;font-size:13px;color:var(--ink);text-decoration:none;font-weight:600}
.main-nav a.active{color:var(--red)}
.admin-btn{left:991px;top:30px;width:110px;height:34px;background:var(--red);color:#fff;font-size:12px;font-weight:600;display:flex;align-items:center;justify-content:center}

/* hero */
.hero{left:0;top:96px;width:1200px;height:526px;background:linear-gradient(100deg,#3d5a7a 0%,#7a6f8c 18%,#5e8a3a 38%,#9fba6a 55%,#cfcfc8 65%,#7aa34a 78%,#4f7d2c 100%)}
.hero-shade{left:0;top:96px;width:1200px;height:526px;background:linear-gradient(90deg,rgba(0,0,0,.35),rgba(0,0,0,0) 60%)}
.hero-arrow{top:330px;width:38px;height:38px;border-radius:50%;background:rgba(255,255,255,.35);display:flex;align-items:center;justify-content:center}
.hero-title{left:101px;top:414px;font-size:24px;font-weight:600;color:#fff}
.hero-text{left:101px;top:456px;width:510px;font-size:15px;font-weight:700;line-height:22px;color:#fff}

/* about */
.about{left:0;top:622px;width:1200px;height:305px;background:var(--light)}
.section-title{font-size:26px;font-weight:600;color:var(--ink);text-align:center;width:1200px;left:0}
.about-text{left:127px;top:698px;width:946px;font-size:12px;line-height:19px;color:var(--body);text-align:center}
.btn{display:flex;align-items:center;justify-content:center;color:#fff;font-size:12px;font-weight:600}

/* packages */
.package{top:1024px;width:194px;height:274px;color:#fff;text-align:center;padding:16px 14px 0}
.package::after{content:"";position:absolute;left:10px;right:10px;bottom:-10px;height:12px;background:radial-gradient(ellipse at center,rgba(0,0,0,.25),rgba(0,0,0,0) 70%)}
.package .price{font-size:24px;font-weight:600;margin-bottom:12px}
.package p{font-size:12px;line-height:20px;font-weight:600}
.view-details{left:145px;top:1273px;width:108px;height:33px;background:var(--brown);color:#fff;font-size:11px;font-weight:600;display:flex;align-items:center;justify-content:center}

/* case studies */
.case-band{left:0;top:1355px;width:1200px;height:352px;background:var(--grey)}
.block-title{font-size:24px;font-weight:600;color:var(--ink);left:96px}
.view-all{width:82px;height:28px;background:var(--orange);color:#fff;font-size:10px;font-weight:600;display:flex;align-items:center;justify-content:center;left:1019px}
.case-card{top:1442px;width:488px;height:216px;background:#fff}
.case-photo{left:25px;top:26px;width:151px;height:166px}
.case-card h3{position:absolute;left:190px;top:22px;width:280px;font-size:15px;line-height:20px;font-weight:600;color:var(--ink)}
.case-card p{position:absolute;left:190px;top:96px;width:280px;font-size:12px;line-height:19px;color:var(--muted)}
.read-more{position:absolute;left:190px;top:176px;font-size:12px;color:var(--red);display:flex;align-items:center;gap:6px}

/* blog */
.blog-card{top:1825px;width:232px;height:248px;background:#fff;border:1px solid #e3e3e3}
.blog-photo{left:0;top:0;width:230px;height:135px}
.date-badge{left:15px;top:14px;width:36px;height:38px;background:#1c1c1c;color:#fff;text-align:center;font-size:8px;font-weight:700;line-height:10px;padding-top:8px}
.blog-card h4{position:absolute;left:10px;top:150px;font-size:13px;font-weight:700;color:var(--ink)}
.blog-card p{position:absolute;left:10px;top:178px;width:212px;font-size:11px;line-height:21px;color:var(--muted)}
.blog-card p b{color:var(--blue);font-weight:600}

/* footer */
.site-footer{left:0;top:2151px;width:1200px;height:461px;background:var(--footer)}
.foot-title{top:2229px;font-family:'Raleway','Open Sans',sans-serif;font-size:14px;font-weight:800;color:#fff;letter-spacing:.3px}
.foot-rule{top:2258px;width:30px;height:2px;background:var(--blue)}
.quick-links a{position:absolute;left:98px;width:139px;font-size:11px;font-weight:600;color:#fff;text-decoration:none;padding-bottom:10px;border-bottom:1px solid var(--line)}
.tweet-box{left:359px;top:2296px;width:289px;height:198px;background:#fff;padding:8px 10px;font-size:10px;color:#333}
.tweet{display:flex;gap:8px;padding:6px 0;border-bottom:1px solid #e8e8e8}
.tweet:last-child{border-bottom:none}
.avatar{width:32px;height:32px;flex:none}
.tweet .who{font-weight:700;font-size:10px}
.tweet .who span{font-weight:400;color:#999}
.tweet .txt{line-height:14px}
.tweet .meta{color:#aaa;font-size:9px;margin-top:3px}
.link{color:var(--blue)}
.news-text{left:766px;top:2294px;width:330px;font-size:11px;line-height:21px;color:#bdbdbd}
.email{left:766px;top:2369px;width:262px;height:40px;background:#333;color:#cfcfcf;font-size:11px;padding-left:16px;display:flex;align-items:center}
.send{left:1028px;top:2369px;width:47px;height:40px;background:var(--blue);display:flex;align-items:center;justify-content:center}
.copyright{left:98px;top:2546px;font-size:11px;color:#9a9a9a}
.legal-bar{left:592px;top:2540px;width:608px;height:42px}
.legal-links a{position:absolute;top:2553px;font-size:11px;color:#bdbdbd;text-decoration:none}
</style>
</head>
<body>

<header class="abs site-header">
  <div class="abs brand">MOVENDRA</div>
  <nav class="main-nav">
    <a class="active" style="left:478px">Home</a>
    <a style="left:552px">About</a>
    <a style="left:626px">Packages</a>
    <a style="left:720px">News</a>
    <a style="left:790px">Case Studies</a>
    <a style="left:905px">Contact Us</a>
  </nav>
  <div class="abs admin-btn">Admin Login</div>
</header>

<section>
  <div class="abs hero" role="img" aria-label="Photo of smiling children playing tug of war on a sunny school field"></div>
  <div class="abs hero-shade"></div>
  <div class="abs hero-arrow" style="left:35px"><svg width="14" height="14" viewBox="0 0 14 14"><path d="M9 2 4 7l5 5" fill="none" stroke="#555" stroke-width="2"/></svg></div>
  <div class="abs hero-arrow" style="left:1126px"><svg width="14" height="14" viewBox="0 0 14 14"><path d="M5 2l5 5-5 5" fill="none" stroke="#555" stroke-width="2"/></svg></div>
  <h1 class="abs hero-title">Welcome To MOVENDRA</h1>
  <p class="abs hero-text">We provide physical education training to schools and deliver interventions to improve health and wellbeing, academic achievement through physical activity.</p>
</section>

<section>
  <div class="abs about"></div>
  <h2 class="abs section-title" style="top:652px">ABOUT US</h2>
  <p class="abs about-text">Wales is facing spiralling health issues including many conditions associated with lack of physical activity and a shortage of skills required for economic growth. The alignment of current complementary cutting edge policies and plans in Wales, such as the 'Well-being of Future Generations (Wales) Act (2015) and Qualified for Life (2014), presents a unique opportunity for a long term collaborative approach to improving the outcomes for people in Wales, particularly those experiencing inequalities and barriers At Movendra Ltd we believe that Physical Literacy is the pivotal foundation to the success of these policies and plans and fundamental to children and young people becoming healthy and confident individuals. Physical Literacy is the motivation, confidence, physical competence, knowledge and understanding to value and take responsibility for engagement in physical activity for life (Harwood 2016).</p>
  <div class="abs btn" style="left:489px;top:848px;width:110px;height:35px;background:var(--red)">Read More</div>
  <div class="abs btn" style="left:603px;top:848px;width:109px;height:35px;background:var(--blue)">Contact</div>
</section>

<section>
  <h2 class="abs section-title" style="top:959px">PACKAGES FOR SCHOOLS</h2>
  <div class="abs package" style="left:99px;background:var(--orange)"><div class="price">£750</div><p>£750 (per day) for whole school inset (full day). This provides schools with two experienced tutors, full day of training and resources.</p></div>
  <div class="abs package" style="left:301px;background:var(--blue)"><div class="price">£375</div><p>£375 for whole school inset (half day/twilight). This provides schools with two experienced tutors, half day of training and resources.</p></div>
  <div class="abs package" style="left:503px;background:var(--mustard)"><div class="price">£350-£500</div><p>£350-£500 (per day) - Consultancy for curriculum development, mentoring support and project development</p></div>
  <div class="abs package" style="left:705px;background:var(--red)"><div class="price">£150</div><p>£150 for a place on a host course (£125 early bird deal). This provides the participant with two experienced tutors delivering the course, full day of training and resources.</p></div>
  <div class="abs package" style="left:907px;background:var(--green)"><div class="price">£200</div><p>£200 for a place at one of our conferences (£175 early bird deal). This provides delegates with a range of engaging workshops delivered by experienced tutors and/or experienced teachers/mentors, lunch and resources and ideas to take away.</p></div>
  <div class="abs view-details">VIEW DETAILS</div>
</section>

<section>
  <div class="abs case-band"></div>
  <h2 class="abs block-title" style="top:1386px">CASE STUDIES</h2>
  <div class="abs view-all" style="top:1390px">VIEW ALL</div>
  <article class="abs case-card" style="left:99px">
    <div class="abs case-photo" role="img" aria-label="Photo of pupils running a relay around cones on a school field" style="background:linear-gradient(180deg,#b9c6cf 0%,#8ea06a 55%,#6f8e3a 100%)"></div>
    <h3>Lorem ipsum dolor sit amet, consectetur adipiscing elit. Nunc quam sapien, volutpat</h3>
    <p>Maecenas feugiat augue risus, vitae pretium lorem cursus ac. Donec ut interdum felis, sit amet scelerisque tellus. Sed non luctus turpis. Donec a efficitur tortor.</p>
    <div class="read-more">Read More <svg width="11" height="11" viewBox="0 0 11 11"><circle cx="5.5" cy="5.5" r="5.5" fill="#ec1f27"/><path d="M4.5 3l2.5 2.5L4.5 8" fill="none" stroke="#fff" stroke-width="1.5"/></svg></div>
  </article>
  <article class="abs case-card" style="left:613px">
    <div class="abs case-photo" role="img" aria-label="Photo of children jumping in a bright classroom" style="background:linear-gradient(135deg,#f2efe6 0%,#e8d9b0 45%,#e9a34a 75%,#c9d9e3 100%)"></div>
    <h3>Lorem ipsum dolor sit amet, consectetur adipiscing elit. Nunc quam sapien, volutpat</h3>
    <p>Maecenas feugiat augue risus, vitae pretium lorem cursus ac. Donec ut interdum felis, sit amet scelerisque tellus. Sed non luctus turpis. Donec a efficitur tortor.</p>
    <div class="read-more">Read More <svg width="11" height="11" viewBox="0 0 11 11"><circle cx="5.5" cy="5.5" r="5.5" fill="#ec1f27"/><path d="M4.5 3l2.5 2.5L4.5 8" fill="none" stroke="#fff" stroke-width="1.5"/></svg></div>
  </article>
</section>

<section>
  <h2 class="abs block-title" style="top:1756px">LATEST BLOG</h2>
  <div class="abs view-all" style="top:1759px">VIEW ALL</div>
  <article class="abs blog-card" style="left:99px">
    <div class="abs blog-photo" role="img" aria-label="Photo of children bouncing on colourful exercise balls" style="background:linear-gradient(180deg,#d9c48a 0%,#e87c3a 50%,#6fae3a 80%,#e6d24a 100%)"></div>
    <div class="abs date-badge">17<br>MAR</div>
    <h4>Blog Post Title Here</h4>
    <p>It is a long established fact that a reader will be distracted by the readable content of a page when looking at its layout. <b>Read More</b></p>
  </article>
  <article class="abs blog-card" style="left:357px">
    <div class="abs blog-photo" role="img" aria-label="Photo of a class in red shirts sitting in a sports hall" style="background:linear-gradient(180deg,#c98f5e 0%,#b86a4a 45%,#d3342c 75%,#a8734e 100%)"></div>
    <div class="abs date-badge">10<br>MAR</div>
    <h4>Blog Post Title Here</h4>
    <p>It is a long established fact that a reader will be distracted by the readable content of a page when looking at its layout. <b>Read More</b></p>
  </article>
  <article class="abs blog-card" style="left:613px">
    <div class="abs blog-photo" role="img" aria-label="Photo of pupils stretching with arms raised in a gym" style="background:linear-gradient(180deg,#b88a5a 0%,#d8c0a0 45%,#efe8de 70%,#7a5a40 100%)"></div>
    <div class="abs date-badge">12<br>FEB</div>
    <h4>Blog Post Title Here</h4>
    <p>It is a long established fact that a reader will be distracted by the readable content of a page when looking at its layout. <b>Read More</b></p>
  </article>
  <article class="abs blog-card" style="left:871px">
    <div class="abs blog-photo" role="img" aria-label="Photo of a girl flexing her arms outdoors" style="background:linear-gradient(180deg,#e7eef0 0%,#d6dde0 45%,#2fb39a 75%,#e8a0a8 100%)"></div>
    <div class="abs date-badge">28<br>JAN</div>
    <h4>Blog Post Title Here</h4>
    <p>It is a long established fact that a reader will be distracted by the readable content of a page when looking at its layout. <b>Read More</b></p>
  </article>
</section>

<footer>
  <div class="abs site-footer"></div>

  <h5 class="abs foot-title" style="left:98px">QUICK LINKS</h5>
  <div class="abs foot-rule" style="left:98px"></div>
  <nav class="quick-links">
    <a style="top:2295px">HOME</a>
    <a style="top:2331px">ABOUT US</a>
    <a style="top:2367px">PRIVACY POLICY</a>
    <a style="top:2403px;border-bottom:none">FAQ</a>
  </nav>

  <h5 class="abs foot-title" style="left:355px">TWITTER FEED</h5>
  <div class="abs foot-rule" style="left:355px"></div>
  <svg class="abs" style="left:630px;top:2232px" width="12" height="20" viewBox="0 0 12 20"><path d="M2 7l4-4 4 4M2 13l4 4 4-4" fill="none" stroke="#33a6d7" stroke-width="1.6"/></svg>
  <div class="abs tweet-box">
    <div style="font-size:8px;color:#aaa">Lars Whitby retweeted</div>
    <div class="tweet">
      <div class="avatar" role="img" aria-label="Profile picture" style="background:#a89a84"></div>
      <div><div class="who">Dorian Pell <span>@DorianPellOn · 9h</span></div>
      <div class="txt">Hey #AppNight fans. Who would come to a tweet-up if it's next Monday evening? #DevNight cc @Brightlane @CodeMeadow @buildfern</div>
      <div class="meta">↩ &nbsp; ⟲ 1 &nbsp; ♥ 3</div></div>
    </div>
    <div class="tweet">
      <div class="avatar" role="img" aria-label="Profile picture" style="background:#2a2a3a"></div>
      <div><div class="who">QuietNotes <span>@quietnotes · 9h</span></div>
      <div class="txt">Science Host Debates Author Tom Reed Happening Now (livestream) <span class="link">go.linkly.com/1boREpe</span></div>
      <div class="meta">↩ &nbsp; ⟲ 47 &nbsp; ♥ 21</div></div>
    </div>
  </div>

  <h5 class="abs foot-title" style="left:766px">NEWSLETTER SIGNUP</h5>
  <div class="abs foot-rule" style="left:766px"></div>
  <p class="abs news-text">If you want receive our all weekly updates about new offers and discount, signup below.</p>
  <div class="abs email">Email Address</div>
  <div class="abs send"><svg width="16" height="16" viewBox="0 0 16 16"><path d="M1 7.5 15 1 11 15 7.5 9.5Z M7.5 9.5 15 1" fill="#fff" stroke="#33a6d7" stroke-width=".8"/></svg></div>

  <div class="abs copyright">Copyright 2016. yoursite All Rights Reserved</div>
  <svg class="abs legal-bar" viewBox="0 0 608 42" preserveAspectRatio="none"><path d="M34 0H608V42H0Z" fill="#1d1d1d"/></svg>
  <nav class="legal-links">
    <a style="left:639px">Terms of Use</a>
    <a style="left:735px">Legal Desclaimer</a>
    <a style="left:855px">Privacy Policy</a>
    <a style="left:955px">Support</a>
    <a style="left:1026px">Sitemap</a>
  </nav>
</footer>

</body>
</html>
```